Real estate investor, needing a business card that communicates warmth, integrity, empathy.

I have a logo that can be manipulated to align with the message - "Serving your home selling needs." Want it to stand out from typical real estate investor cards, and make distressed home sellers feel a connection with me. Should communicate warmth, integrity, empathy, and trustworthiness.

Target Market(s)

Distressed home owners who need to sell their homes, not using realtors.

Contact Information for Business Card

Glossy front and matte back, with a small box that is labelled "notes." I like darker blues and blacks together, but doesn't have to be, as long as it communicates trustworthiness, and a strong call to action.

Other font styles liked:
• see "must haves" above, but willing to review whatever comes my way.

Requirements
Must have
• The fonts on my logo are Aviano, Lusitana, and Marcellus. We don't have to use those, but I favor them.

```html
<!DOCTYPE html>
<html lang="en">
<head>
<meta charset="utf-8">
<title>Harbor Lane Homes – Business Card</title>
<link rel="stylesheet" href="https://fonts.googleapis.com/css2?family=Lusitana:wght@400;700&display=swap">
<style>
  :root {
    --stage: #2b2b2b;
    --paper: #ffffff;
    --ink: #151515;
    --bronze: #a0744c;
    --rule: #333333;
  }
  * { box-sizing: border-box; margin: 0; padding: 0; }
  html, body { width: 1200px; height: 880px; overflow: hidden; }
  body {
    background: var(--stage);
    font-family: "Lusitana", Georgia, serif;
    color: var(--ink);
    position: relative;
  }
  .card {
    position: absolute;
    left: 320px;
    width: 560px;
    height: 320px;
    background: var(--paper);
    border-radius: 18px;
    overflow: hidden;
  }
  .card--notes { top: 90px; }
  .card--front { top: 470px; }

  .brand {
    position: absolute;
    display: flex;
    align-items: center;
    gap: 10px;
    font-size: 30px;
    letter-spacing: 1px;
    color: var(--ink);
    white-space: nowrap;
  }
  .brand__mark {
    width: 12px; height: 12px;
    background: var(--bronze);
  }

  /* Notes side */
  .card--notes .brand { top: 52px; left: 50%; transform: translateX(-50%); }
  .notes__label {
    position: absolute; top: 118px; width: 100%;
    text-align: center; font-size: 20px; letter-spacing: 1px;
  }
  .notes__line {
    position: absolute; left: 50px; right: 50px;
    border-top: 2px dotted var(--rule);
  }
  .notes__line--one { top: 178px; }
  .notes__line--two { top: 218px; }
  .notes__tagline {
    position: absolute; top: 250px; width: 100%;
    text-align: center; font-size: 16px;
  }

  /* Front side */
  .front__art { position: absolute; inset: 0; }
  .card--front .brand { top: 110px; left: 40px; }
  .person { position: absolute; top: 30px; right: 40px; text-align: right; }
  .person__name { font-size: 22px; font-weight: 700; letter-spacing: 1px; }
  .person__title { font-size: 16px; color: var(--bronze); }
  .contact {
    position: absolute; right: 28px; top: 188px;
    color: var(--paper); font-size: 13px; line-height: 1.4; text-align: right;
    white-space: nowrap;
  }
  .contact__address { margin-bottom: 6px; margin-right: 24px; }
  .contact__row { display: flex; justify-content: flex-end; align-items: center; gap: 8px; }
  .contact__icon { width: 16px; height: 16px; flex: none; }
</style>
</head>
<body>

<section class="card card--notes" aria-label="Card back with notes area">
  <div class="brand"><span class="brand__mark"></span>Harbor Lane Homes</div>
  <p class="notes__label">NOTE</p>
  <div class="notes__line notes__line--one"></div>
  <div class="notes__line notes__line--two"></div>
  <p class="notes__tagline">Serving Your Home Selling Needs.</p>
</section>

<section class="card card--front" aria-label="Card front">
  <svg class="front__art" viewBox="0 0 560 320" aria-hidden="true">
    <path d="M560,96 C440,96 380,130 350,180 C315,245 270,300 150,320 L560,320 Z" fill="var(--ink)"/>
    <path d="M520,106 C420,112 366,146 336,194 C300,256 258,302 168,316" fill="none" stroke="var(--paper)" stroke-width="4"/>
    <path d="M310,200 C292,266 226,294 110,288 L110,302 C250,312 316,278 310,200 Z" fill="var(--bronze)"/>
  </svg>

  <div class="brand"><span class="brand__mark"></span>Harbor Lane Homes</div>

  <div class="person">
    <p class="person__name">DANIEL R. MOORE</p>
    <p class="person__title">Executive Director</p>
  </div>

  <div class="contact">
    <p class="contact__address">PO Box 48 Elm Row<br>14 Mill St, Dayton, USA</p>
    <p class="contact__row">555-210-4836
      <svg class="contact__icon" viewBox="0 0 16 16" aria-hidden="true"><circle cx="8" cy="8" r="8" fill="var(--bronze)"/><path d="M5 4.5l1.6-.5 1 2-1 .8a5 5 0 0 0 2.6 2.6l.8-1 2 1-.5 1.6C8 11 5 8 5 4.5z" fill="var(--paper)"/></svg>
    </p>
    <p class="contact__row">info@harborlane.com
      <svg class="contact__icon" viewBox="0 0 16 16" aria-hidden="true"><circle cx="8" cy="8" r="8" fill="var(--bronze)"/><rect x="4" y="5" width="8" height="6" fill="var(--paper)"/><path d="M4 5l4 3.2L12 5" fill="none" stroke="var(--bronze)" stroke-width="1"/></svg>
    </p>
    <p class="contact__row">www.harborlane.com
      <svg class="contact__icon" viewBox="0 0 16 16" aria-hidden="true"><circle cx="8" cy="8" r="8" fill="var(--bronze)"/><circle cx="8" cy="8" r="4" fill="none" stroke="var(--paper)" stroke-width="1"/><ellipse cx="8" cy="8" rx="1.8" ry="4" fill="none" stroke="var(--paper)" stroke-width="1"/><path d="M4 8h8" stroke="var(--paper)" stroke-width="1"/></svg>
    </p>
  </div>
</section>

</body>
</html>
```